Web site for fans of TV series "The Drifter Pass"

1. Description: This is a new web site for the fans of a Western TV series called "The Drifter Pass". It ran for nine seasons from 1962 to 1971.

It is going to be a fan-generated content. The site will use a proprietary social-sharing software in the back-end. The software could be looked as your personal Chatterbox service running on your own domain. In fact, anyone can use this software for any social-sharing need.

A sample of the software running a social-sharing site:
http://www.valtemo.com

The public-facing software has ten sections or modules as follows:

1. Survey
2. Blog
3. Links
4. Video
5. Music
6. Photo
7. Cartoon
8. Photo Album
9. Quotes
10. Follow/Followers (like squawkr)

2. Delivery. Three designs for three pages. I need delivery in PSD, JPG and AI formats..

3. Pages

3.1. Homepage
Example: http://www.valtemo.com

IMPORTANT REQUIREMENT. The Homepage should be designed such that I or the site Admin with basic knowledge of HTML and CSS can move around different sections or modules without a need to rewrite the CSS or HTML code.

3.2. Point of Entry or Summary page.
Example: http://valtemo.com/vksp/blog/latest/

3.3. Detail page
Example: http://valtemo.com/vksp/blog/2929/

Project Deadline Extended
Reason: I received acceptable designs late. I would like to give this contest 7 more days. This gives me time to work with current designs and just in case I receive new designs.

Target Market(s)

Age: Above 40, average age is 50-55

Gender: Primarily female

Location: Primarily United States, but we have a visible following in Europe and South America.

Industry/Entity Type

Tv

Requirements
Must have
• 1. The image/icon of The Drifter Pass. You can capture it via ClipHollow clips at the opening of the show.

2. Red color (burgundy. See shirt of the main character called Drifter played by actor Walter Penhale.

3. The American West spirit (yes, you may call it the cowboy spirit)

4. The Homepage should be designed such that a person with basic knowledge of CSS and HTML coding can move around different sections or modules.
Should not have
• No cartoonish icons.

```html
<!DOCTYPE html>
<html lang="en">
<head>
<meta charset="utf-8">
<title>The Drifter Pass Wiki</title>
<link rel="stylesheet" href="https://fonts.googleapis.com/css2?family=Arimo:wght@400;700&family=Rokkitt:wght@400;700&family=Signika:wght@300;400&display=swap">
<style>
:root{
  --burgundy-dark:#1c0609;
  --burgundy:#5a0f1a;
  --burgundy-mid:#7a1a26;
  --gold:#c9a36a;
  --frame:#8e5c31;
  --frame-dark:#6b3f1e;
  --ink:#3c2a1c;
  --red-text:#8c1b1b;
  --footer:#3b2311;
  --footer-link:#d7a75e;
  --road:#c07a4e;
  --video:#232323;
}
*{box-sizing:border-box;margin:0;padding:0}
html,body{width:707px;height:1200px;overflow:hidden}
body{position:relative;font-family:"Arimo",Arial,sans-serif;color:var(--ink);
  background:linear-gradient(#efdcb6 0,#e8cfa2 300px,#dcb98a 640px,#d9b285 100%)}
a{color:inherit;text-decoration:none}
h2,h4{font-weight:400}

/* top bar */
.topbar{position:absolute;left:0;top:0;width:707px;height:33px;z-index:3;
  background:linear-gradient(var(--burgundy-dark),#3b0c13);border-bottom:2px dotted var(--gold)}
.brand{position:absolute;left:67px;top:6px;display:flex;align-items:center;gap:6px;
  font-family:"Rokkitt",Georgia,serif;font-weight:700;color:#fff}
.brand-mark{width:30px;height:21px;background:#b7803f;border:1px solid #e8d3a8}
.brand-name{font-size:12.5px}
.brand-name small{font-size:8.5px}
.account{position:absolute;right:66px;top:11px;font-size:8px;color:#fff;word-spacing:1px}

/* hero */
.hero{position:absolute;left:0;top:35px;width:707px;height:236px;
  background:linear-gradient(180deg,#8d9460 0%,#a89869 30%,#b79f78 55%,#8b6a47 80%,#9c7d59 100%)}

/* section nav */
.section-nav{position:absolute;left:0;top:271px;width:707px;height:36px;
  background:linear-gradient(#6e1422,#4a0a14 60%,#3a0810);
  border-top:2px solid var(--gold);border-bottom:2px solid var(--gold);
  font-family:"Rokkitt",Georgia,serif;font-size:13px;font-weight:400;color:#f3e3c6}
.nav-item{position:absolute;top:8px;display:flex;align-items:center;gap:7px}
.nav-icon{width:15px;height:13px;border-radius:2px}
.nav-pages{position:absolute;left:600px;top:11px;font-family:"Arimo",sans-serif;font-size:9px;display:flex;gap:4px;align-items:center}
.nav-pages i{display:inline-block;width:8px;height:8px;border:1px solid #f3e3c6;border-radius:50%}

/* landscape sits behind panels */
.landscape{position:absolute;left:0;top:958px;width:707px;height:118px;z-index:0;
  background:linear-gradient(#dcb88a,#cfa571 70%,#b8854e)}

/* panels */
.panel{position:absolute;z-index:2;border:2px solid var(--frame);padding:3px;
  background:linear-gradient(#d6b07c,#c49a66);box-shadow:0 1px 3px rgba(60,30,10,.35)}
.panel-inner{height:100%;border:3px double var(--frame-dark);outline:1px dotted #a4713f;outline-offset:-6px;
  background:radial-gradient(ellipse at 50% 40%,#f8ecd1 0%,#efd9b0 60%,#e0bf8d 100%);position:relative}
.panel-title{position:absolute;left:10px;top:13px;font-family:"Signika",sans-serif;font-size:10px;color:#6a1f1f}

.avatar{width:20px;height:20px;border-radius:50%;background:#a9927b;border:1px solid #fff;flex:none}
.small{font-size:6.5px;color:var(--ink)}
.meta{font-size:6.5px;color:var(--red-text)}
.time{font-size:6.3px;color:var(--ink)}

.votes{display:flex;align-items:center;gap:3px;font-size:7.5px;color:var(--red-text)}
.thumb{width:9px;height:9px;border:1px solid #7b7b7b;border-radius:2px;background:#f1ead9}
.thumb.up{border-color:var(--red-text);background:#c23a3a}
.meter{width:30px;height:3px;background:#c9b89b;position:relative}
.meter b{position:absolute;left:0;top:0;height:3px;background:var(--burgundy-mid)}
.pager{display:flex;gap:3px;font-size:8px;color:var(--red-text)}
.pager-arrows{display:flex;width:34px;height:14px;background:#2a2522}
.pager-arrows span{flex:1;color:#ddd;font-size:6px;text-align:center;line-height:14px}

/* blog posts */
.post{position:absolute;left:13px;width:240px}
.post .avatar{position:absolute;left:0;top:2px}
.post-text{position:absolute;left:28px;top:0;width:165px;font-size:6.8px;line-height:10px}
.post-time{position:absolute;left:200px;top:0;font-size:6.3px}
.post .meta{position:absolute;left:28px;top:23px}
.post .votes{position:absolute;left:28px;top:38px}

/* photo tiles */
.tile{position:absolute;width:111px}
.tile-img{height:70px}
.caption{margin-top:4px;font-size:6.8px;color:var(--red-text);line-height:10px}
.caption .time{float:right}
.byline{display:flex;gap:8px;margin-top:2px;align-items:center}
.byline div{line-height:10px}

/* videos */
.video{position:absolute;width:119px}
.player{height:96px;background:var(--video);position:relative;border:1px solid #111}
.player .play{position:absolute;left:45px;top:30px;width:28px;height:28px;border-radius:50%;background:#555;
  display:flex;align-items:center;justify-content:center}
.player .bar{position:absolute;left:0;bottom:0;width:100%;height:9px;background:#0f0f0f;border-top:1px solid #333}
.player .bar b{position:absolute;left:18px;top:3px;width:85px;height:2px;background:#3a5f8f}
.video-head{display:flex;gap:8px;font-size:6.8px;margin-top:6px}
.video-head span:first-child{color:var(--red-text)}

/* quote */
.quote{position:absolute;left:17px;top:70px;width:250px;font-family:"Signika",sans-serif;font-weight:300;font-size:12.4px;line-height:16px;color:#6a1818}
.quote-by{position:absolute;right:14px;top:143px;font-family:"Signika",sans-serif;font-weight:300;font-size:9.5px;color:#5a1a1a}

/* footer */
.footer{position:absolute;left:0;top:1076px;width:707px;height:124px;z-index:1;background:var(--footer);border-top:1px solid #6e4422}
.road{position:absolute;left:70px;top:1076px;width:170px;height:124px;z-index:1;
  background:var(--road);clip-path:polygon(55% 0,85% 0,55% 45%,20% 100%,0 100%,0 80%)}
.footer-text{position:absolute;z-index:2}
.footer-col{top:1113px;font-size:6.8px;color:var(--footer-link);line-height:13.5px}
.footer-col h4{font-size:9px;color:#fff;margin-bottom:1px}
.copyright{left:58px;top:1184px;font-size:7px;color:var(--footer-link)}
.social{right:64px;top:1184px;font-size:6.5px;color:#d9c6a8;display:flex;gap:6px}
</style>
</head>
<body>

<header class="topbar">
  <a class="brand" href="#"><span class="brand-mark"></span><span class="brand-name">THE DRIFTER PASS <small>Wiki</small></span></a>
  <nav class="account"><a href="#">Login</a> | <a href="#">Register</a> | <a href="#">Post It ▾</a></nav>
</header>

<div class="hero" role="img" aria-label="Photograph of a western ranch set with wooden barns, a windmill and a ranch house on a hillside"></div>

<nav class="section-nav">
  <a class="nav-item" href="#" style="left:67px"><span class="nav-icon" style="background:#e2781f"></span>Blogs</a>
  <a class="nav-item" href="#" style="left:165px"><span class="nav-icon" style="background:#d79a2a"></span>Photos</a>
  <a class="nav-item" href="#" style="left:275px"><span class="nav-icon" style="background:#e9c21d;border-radius:50%"></span>Quotes</a>
  <a class="nav-item" href="#" style="left:375px"><span class="nav-icon" style="background:#6f93b6"></span>Photos Albums</a>
  <a class="nav-item" href="#" style="left:513px"><span class="nav-icon" style="background:#c23232"></span>Videos</a>
  <div class="nav-pages"><i></i>1 <span>|</span> 2<i></i></div>
</nav>

<div class="landscape" role="img" aria-label="Illustrated desert landscape with hills, clouds, a hawk, poplar trees and a signpost reading The Drifter Pass"></div>

<!-- Blog Posts -->
<section class="panel" style="left:66px;top:326px;width:279px;height:299px">
  <div class="panel-inner">
    <h2 class="panel-title">Blog Posts</h2>
    <article class="post" style="top:34px">
      <span class="avatar"></span>
      <p class="post-text">Lorem Ipsum is simply dummy text of the printing and typesetting industry. <span class="small">Unkown</span></p>
      <span class="post-time">7 hours ago</span>
      <p class="meta">65 Views | 2 Comments: latest by hamal 4 hours ago</p>
      <div class="votes"><span class="thumb up"></span>6<span class="meter"><b style="width:22px"></b></span>0<span class="thumb"></span></div>
    </article>
    <article class="post" style="top:90px">
      <span class="avatar"></span>
      <p class="post-text">Lorem Ipsum is simply dummy text of the printing and typesetting industry. <span class="small">Unkown</span></p>
      <span class="post-time">7 hours ago</span>
      <p class="meta">65 Views | 2 Comments: latest by hamal 4 hours ago</p>
      <div class="votes"><span class="thumb up"></span>5<span class="meter"><b style="width:20px"></b></span>0<span class="thumb"></span></div>
    </article>
    <article class="post" style="top:146px">
      <span class="avatar"></span>
      <p class="post-text">Lorem Ipsum is simply dummy text of the printing and typesetting industry. <span class="small">Unkown</span></p>
      <span class="post-time">7 hours ago</span>
      <p class="meta">65 Views | 2 Comments: latest by hamal 4 hours ago</p>
      <div class="votes"><span class="thumb up"></span>4<span class="meter"><b style="width:17px"></b></span>0<span class="thumb"></span></div>
    </article>
    <article class="post" style="top:202px">
      <span class="avatar"></span>
      <p class="post-text">Lorem Ipsum is simply dummy text of the printing and typesetting industry. <span class="small">Unkown</span></p>
      <span class="post-time">7 hours ago</span>
      <p class="meta">65 Views | 2 Comments: latest by hamal 4 hours ago</p>
      <div class="votes"><span class="thumb up"></span>2<span class="meter"><b style="width:8px"></b></span>0<span class="thumb"></span></div>
    </article>
    <div class="pager" style="position:absolute;left:10px;top:265px">1 | 2 | 3 | 4 | 5 | 6 | 7 | .... |16</div>
    <div class="pager-arrows" style="position:absolute;left:220px;top:262px"><span>◀</span><span>▶</span></div>
  </div>
</section>

<!-- Photos -->
<section class="panel" style="left:66px;top:632px;width:279px;height:190px">
  <div class="panel-inner">
    <h2 class="panel-title">Photos</h2>
    <article class="tile" style="left:11px;top:30px">
      <div class="tile-img" role="img" aria-label="Photo of three cast members in western costume" style="background:linear-gradient(135deg,#c8a88a,#8a6a58 60%,#5a5a6a)"></div>
      <p class="caption"><span class="time">7 hours ago</span>Lorem Ipsum is simply dummy text of the printing.</p>
      <div class="byline"><span class="avatar"></span><div class="small">Unkown<br>65 Views | 2 Comments</div></div>
      <div class="votes" style="margin-top:6px"><span class="thumb up"></span>0<span class="meter"></span>5<span class="thumb"></span></div>
    </article>
    <article class="tile" style="left:140px;top:30px">
      <div class="tile-img" role="img" aria-label="Promotional photo of the lead actor in a hat with his name lettered below" style="background:linear-gradient(#9a6a3a,#c08850 55%,#3a2a1f)"></div>
      <p class="caption"><span class="time">7 hours ago</span>Lorem Ipsum is simply dummy text of the printing.</p>
      <div class="byline"><span class="avatar"></span><div class="small">Unkown<br>65 Views | 2 Comments</div></div>
      <div class="votes" style="margin-top:6px"><span class="thumb up"></span>5<span class="meter"><b style="width:22px"></b></span>0<span class="thumb"></span></div>
    </article>
  </div>
</section>

<!-- Picture Albums -->
<section class="panel" style="left:66px;top:831px;width:279px;height:123px">
  <div class="panel-inner">
    <h2 class="panel-title" style="top:12px">Picture Albums</h2>
    <div role="img" aria-label="Strip of three album photos from the series" style="position:absolute;left:11px;top:27px;width:243px;height:45px;display:flex;gap:3px">
      <span style="flex:1;background:linear-gradient(#6a4a5a,#b2405a)"></span>
      <span style="flex:1;background:linear-gradient(#a88060,#7a4a30)"></span>
      <span style="flex:1;background:linear-gradient(#b99770,#6a4a30)"></span>
    </div>
    <span style="position:absolute;left:11px;top:45px;width:10px;height:10px;background:#fff;font-size:7px;text-align:center;line-height:10px">◀</span>
    <span style="position:absolute;left:244px;top:45px;width:10px;height:10px;background:#fff;font-size:7px;text-align:center;line-height:10px">▶</span>
    <p style="position:absolute;left:11px;top:76px;font-size:7.5px;color:var(--red-text)">Walter Penhale <span class="time">7 hours ago</span></p>
    <div class="byline" style="position:absolute;left:11px;top:84px"><span class="avatar"></span><div class="small">Unkown<br>65 Views | 2 Comments</div></div>
    <div class="votes" style="position:absolute;left:170px;top:90px"><span class="thumb up"></span>5<span class="meter"><b style="width:22px"></b></span>0<span class="thumb"></span></div>
  </div>
</section>

<!-- Videos -->
<section class="panel" style="left:363px;top:326px;width:280px;height:406px">
  <div class="panel-inner">
    <h2 class="panel-title">Videos</h2>
    <article class="video" style="left:10px;top:33px">
      <div class="player"><span class="play"><svg width="10" height="12"><path d="M0 0L10 6L0 12Z" fill="#fff"/></svg></span><span class="bar"><b></b></span></div>
      <p class="video-head"><span>Video Heading 1</span><span>10 hours Ago</span></p>
      <div class="byline"><span class="avatar"></span><div class="small">James_ Shawn<br>3 Views | 0 Comments</div></div>
      <div class="votes" style="margin-top:6px"><span class="thumb up"></span>2<span class="meter"><b style="width:14px"></b></span>3<span class="thumb"></span></div>
    </article>
    <article class="video" style="left:134px;top:33px">
      <div class="player"><span class="play"><svg width="10" height="12"><path d="M0 0L10 6L0 12Z" fill="#fff"/></svg></span><span class="bar"><b></b></span></div>
      <p class="video-head"><span>Video Heading 1</span><span>10 hours Ago</span></p>
      <div class="byline"><span class="avatar"></span><div class="small">James_ Shawn<br>3 Views | 0 Comments</div></div>
      <div class="votes" style="margin-top:6px"><span class="thumb up"></span>3<span class="meter"><b style="width:14px"></b></span>2<span class="thumb"></span></div>
    </article>
    <article class="video" style="left:10px;top:201px">
      <div class="player"><span class="play"><svg width="10" height="12"><path d="M0 0L10 6L0 12Z" fill="#fff"/></svg></span><span class="bar"><b></b></span></div>
      <p class="video-head"><span>Video Heading 1</span><span>10 hours Ago</span></p>
      <div class="byline"><span class="avatar"></span><div class="small">James_ Shawn<br>3 Views | 0 Comments</div></div>
      <div class="votes" style="margin-top:6px"><span class="thumb up"></span>0<span class="meter"></span>3<span class="thumb"></span></div>
    </article>
    <article class="video" style="left:134px;top:201px">
      <div class="player"><span class="play"><svg width="10" height="12"><path d="M0 0L10 6L0 12Z" fill="#fff"/></svg></span><span class="bar"><b></b></span></div>
      <p class="video-head"><span>Video Heading 1</span><span>10 hours Ago</span></p>
      <div class="byline"><span class="avatar"></span><div class="small">James_ Shawn<br>3 Views | 0 Comments</div></div>
      <div class="votes" style="margin-top:6px"><span class="thumb up"></span>3<span class="meter"><b style="width:24px"></b></span>0<span class="thumb"></span></div>
    </article>
    <div class="pager" style="position:absolute;left:10px;top:371px">1 | 2 | 3 | 4 | 5 | 6 | 7 | .... |16</div>
    <div class="pager-arrows" style="position:absolute;left:221px;top:368px"><span>◀</span><span>▶</span></div>
  </div>
</section>

<!-- Quotes -->
<section class="panel" style="left:363px;top:741px;width:280px;height:227px">
  <div class="panel-inner">
    <h2 class="panel-title" style="top:20px">Quotes</h2>
    <blockquote class="quote">I always turn to the sports pages first,<br>which records people's accomplishments.<br>The front page...</blockquote>
    <p class="quote-by">~ Ezra Whitcombe ~</p>
    <p class="small" style="position:absolute;left:28px;top:177px">3 Views | 0 Comments</p>
    <div class="votes" style="position:absolute;left:167px;top:187px"><span class="thumb up"></span>6<span class="meter"><b style="width:24px"></b></span>0<span class="thumb"></span></div>
  </div>
</section>

<footer class="footer"></footer>
<div class="road" role="img" aria-label="Illustrated winding dirt road with a lone rider on horseback"></div>

<nav class="footer-text footer-col" style="left:260px"><h4>Introduction</h4>- Navigation Link 1<br>- Navigation Link 2<br>- Navigation Link 3</nav>
<nav class="footer-text footer-col" style="left:340px"><h4>You &amp; Us</h4>- Navigation Link 1<br>- Navigation Link 2<br>- Navigation Link 3</nav>
<nav class="footer-text footer-col" style="left:419px"><h4>Policy</h4>- Navigation Link 1<br>- Navigation Link 2<br>- Navigation Link 3</nav>
<nav class="footer-text footer-col" style="left:501px"><h4>Terms of Use</h4>- Navigation Link 1<br>- Navigation Link 2<br>- Navigation Link 3</nav>
<nav class="footer-text footer-col" style="left:580px"><h4>Contact</h4>- Navigation Link 1<br>- Navigation Link 2<br>- Navigation Link 3</nav>

<p class="footer-text copyright">© 2012 - 2013 &nbsp;The Drifter Pass | All Rights Reserved</p>
<nav class="footer-text social"><a href="#">Chatterbox</a><a href="#">squawkr</a><a href="#">ClipHollow</a><a href="#">Linkfold</a><a href="#">Plusring</a></nav>

</body>
</html>
```